Dog Food Bag Packaging Redesign

Hey there..We're a small dog food company, focusing on all natural, locally sourced, high quality ingredients. They're patties, and baked for 10 min. Dogs go insane for them. We're looking to redo our packaging, and thus, its design. I've attached images. Currently, we are wrapping 12 patties in a poly bag and then butcher paper, and sticking a label on it. We're moving to a zipper seal poly that's black. I've attached the design concept from our bag manufacturer for your reference only. We don't necessarily want to use our old label, but we're not against using elements of it. We really like our current label.. I'm just not so sure it's the right call for a poly bag.We have three flavours; chicken, beef, lamb. I would LOVE to know what flavour the bag is without having to be super close to the bag. So perhaps the top part (1-4 inches) could be the flavour colour? I will have to provide some verbiage for the back. I need to add feeding instructions, and a bit of a thank you story. I'm open for suggestions on how to display ingredients/nutritional facts.

Target Market(s)

Dog Owners

Industry/Entity Type

Manufacturing

Font styles to use
Sans Serif

Colors
9bcb3c

Requirements
Must have
• Total bag design. When you submit your design, please submit your designs on top of a bag. It makes it much easier to visual the end product.
• The bag needs to have the associated flavour colours on it to differentiate flavour from a distance. Red = beef, yellow = chicken, purple = lamb.
• I'm happy with the logo being on the back only, but if on the front it needs to be small. Patties should be the main header word.
Nice to have
• I like the idea of a vertical colour bar on the side of the bag to show its flavour, but I'm not again a top horizontal bar either.
• I like PATTIES being the biggest word on the bag.

```html
<!DOCTYPE html>
<html lang="en">
<head>
<meta charset="utf-8">
<title>Patties Pouch Range</title>
<link rel="stylesheet" href="https://fonts.googleapis.com/css2?family=Ubuntu:wght@400;500;700&family=Patrick+Hand&display=swap">
<style>
  :root {
    --stage: #ede6e1;
    --beef-top: #d9443f;
    --beef-body: #f2bcbc;
    --lamb-top: #b07cc6;
    --lamb-body: #dfc8e6;
    --chicken-top: #dcc77a;
    --chicken-body: #ebe9a6;
    --band: #a9db96;
    --green-text: #5fae3c;
    --brown: #b8894a;
    --beef-word: #d9443f;
    --lamb-word: #a865c2;
    --dog-tone: #d49a55;
  }
  * { box-sizing: border-box; margin: 0; padding: 0; }
  html, body { width: 1200px; height: 709px; overflow: hidden; }
  body { background: var(--stage); font-family: "Ubuntu", sans-serif; position: relative; }

  .pouch { position: absolute; top: 55px; width: 340px; height: 600px; border-radius: 6px; overflow: hidden; }
  .pouch--beef { left: 40px; }
  .pouch--lamb { left: 430px; }
  .pouch--chicken { left: 820px; }

  .pouch__top { position: absolute; left: 0; right: 0; top: 0; height: 95px; }
  .pouch__body { position: absolute; left: 0; right: 0; top: 95px; bottom: 0; }
  .pouch--beef .pouch__top { background: var(--beef-top); }
  .pouch--beef .pouch__body { background: var(--beef-body); }
  .pouch--lamb .pouch__top { background: var(--lamb-top); }
  .pouch--lamb .pouch__body { background: var(--lamb-body); }
  .pouch--chicken .pouch__top { background: var(--chicken-top); }
  .pouch--chicken .pouch__body { background: var(--chicken-body); }

  .label { position: absolute; left: 28px; right: 28px; top: 170px; height: 300px; border: 2px solid var(--brown); color: var(--brown); }
  .label__sub { position: absolute; left: 12px; top: 12px; font-size: 14px; }
  .label__title { position: absolute; left: 10px; top: 28px; font-size: 44px; font-weight: 500; color: var(--green-text); }
  .brand { position: absolute; right: 14px; top: 40px; font-size: 13px; font-weight: 400; color: var(--brown); white-space: nowrap; }
  .label__band { position: absolute; left: 0; right: 0; top: 92px; height: 48px; background: var(--band); display: flex; align-items: center; justify-content: center; font-size: 34px; font-weight: 700; }
  .pouch--beef .label__band { color: var(--beef-word); }
  .pouch--lamb .label__band { color: var(--lamb-word); }
  .ingredients { position: absolute; left: 12px; top: 150px; list-style: none; font-size: 15px; line-height: 17px; }
  .dog-art { position: absolute; right: 14px; top: 150px; width: 92px; height: 70px; border-radius: 40% 40% 45% 45%; background: radial-gradient(circle at 50% 60%, #fbf3ec 0 45%, var(--dog-tone) 46%); }
  .pack-size { position: absolute; right: 12px; top: 236px; text-align: right; font-size: 14px; font-weight: 500; color: var(--green-text); line-height: 16px; }
  .tagline { position: absolute; left: 12px; bottom: 10px; font-size: 13px; color: var(--green-text); }

  .back-label { position: absolute; left: 26px; right: 26px; top: 150px; height: 300px; border: 2px solid var(--brown); color: var(--brown); font-size: 9px; line-height: 11px; padding: 10px; }
  .back-label strong { color: var(--green-text); font-weight: 700; }
  .back-label p { margin-bottom: 8px; }
  .back-footer { position: absolute; left: 10px; right: 10px; bottom: 10px; height: 90px; }
  .back-footer .dog-art { left: 0; top: 0; right: auto; width: 54px; height: 40px; }
  .back-footer .brand { right: auto; left: 100px; top: 14px; font-size: 10px; }
  .thanks { position: absolute; left: 0; bottom: 0; font-family: "Patrick Hand", cursive; font-size: 17px; line-height: 17px; color: var(--brown); }
  .nutrition { position: absolute; right: 0; bottom: 0; width: 110px; font-size: 8px; line-height: 10px; }
  .nutrition h3 { font-size: 9px; color: var(--green-text); font-weight: 700; }
  .nutrition table { width: 100%; border-collapse: collapse; }
  .nutrition td:last-child { text-align: right; }
</style>
</head>
<body>

  <section class="pouch pouch--beef">
    <div class="pouch__top"></div>
    <div class="pouch__body" role="img" aria-label="Scattered doodle pattern of cows, eggs, apples, broccoli, carrots, bones and paw prints"></div>
    <div class="label">
      <span class="label__sub">Grass-fed Beef</span>
      <h1 class="label__title">Patties</h1>
      <div class="brand">Bright Bowl</div>
      <div class="label__band">Beef</div>
      <ul class="ingredients"><li>grass-fed beef</li><li>fresh eggs</li><li>apples</li><li>sweet potatoes</li><li>broccoli</li><li>carrots</li></ul>
      <div class="dog-art" role="img" aria-label="Drawing of a happy dog"></div>
      <div class="pack-size">3 lb<br>12 patties</div>
      <span class="tagline">Fresh Local Responsible</span>
    </div>
  </section>

  <section class="pouch pouch--lamb">
    <div class="pouch__top"></div>
    <div class="pouch__body" role="img" aria-label="Scattered doodle pattern of sheep, eggs, apples, broccoli, carrots, bones and paw prints"></div>
    <div class="label">
      <span class="label__sub">Deboned Lamb</span>
      <h1 class="label__title">Patties</h1>
      <div class="brand">Bright Bowl</div>
      <div class="label__band">Lamb</div>
      <ul class="ingredients"><li>deboned lamb</li><li>fresh eggs</li><li>apples</li><li>sweet potatoes</li><li>broccoli</li><li>carrots</li></ul>
      <div class="dog-art" role="img" aria-label="Drawing of a happy dog"></div>
      <div class="pack-size">3 lb<br>12 patties</div>
      <span class="tagline">Fresh Local Responsible</span>
    </div>
  </section>

  <section class="pouch pouch--chicken">
    <div class="pouch__top"></div>
    <div class="pouch__body" role="img" aria-label="Scattered doodle pattern of chickens, eggs, apples, broccoli, carrots, bones and paw prints"></div>
    <div class="back-label">
      <p><strong>Ingredients:</strong> deboned chicken (muscles &amp; organ meat), fresh eggs, apples, sweet potatoes, broccoli, carrots, rolled oats, water, oat flour, brown rice flour, organic spelt flour, wild alaskan salmon oil, supplement (vitamins &amp; minerals), blackstrap molasses</p>
      <p><strong>Feeding instructions:</strong> Serve one patty per 10 lb of body weight daily, split across two meals. Thaw in the fridge overnight and keep sealed after opening. Always leave fresh water out. Adjust portions to your dog's age, activity and body condition.</p>
      <div class="back-footer">
        <div class="dog-art" role="img" aria-label="Drawing of a happy dog"></div>
        <div class="brand">Bright Bowl</div>
        <div class="thanks">Thank you<br>for chosing us!</div>
        <div class="nutrition">
          <h3>Nutrition Facts:</h3>
          <span>per 100g</span>
          <table>
            <tr><td>protein</td><td>18.43%</td></tr>
            <tr><td>fat</td><td>9.84%</td></tr>
            <tr><td>fibre</td><td>0.6%</td></tr>
            <tr><td>calories</td><td>224</td></tr>
            <tr><td>moisture</td><td>49.2%</td></tr>
            <tr><td>dry matter</td><td>49.7%</td></tr>
          </table>
        </div>
      </div>
    </div>
  </section>

</body>
</html>
```